One page, two sided flyer about our company needed for a conference

We are an IT consulting company and need a two sided flyer produced for our company that we are going to hand out to potential clients at a conference we have coming up.

We would like the design to be in-line with the look and feel of our current website design: www.vorquinexa.example

Our logo has been attached along with some screenshots from our site that we would like included.

Target Market(s)

Business Executives

Industry/Entity Type

It Company

Font styles to use
Sans Serif

Colors
ec1f27

```html
<!DOCTYPE html>
<html lang="en">
<head>
<meta charset="utf-8">
<title>Vorquinexa Solutions – Conference Flyer</title>
<link rel="stylesheet" href="https://fonts.googleapis.com/css2?family=Roboto:wght@300;400;500;700&display=swap">
<style>
:root{
  --brand-red:#ec1f27;
  --ink:#2b2b2d;
  --footer-dark:#1d1d1f;
  --stage-light:#d1d2d4;
  --stage-dark:#6d6e71;
  --band-gray:#cdced0;
  --white:#ffffff;
}
*{margin:0;padding:0;box-sizing:border-box}
html,body{width:1200px;height:859px;overflow:hidden}
body{
  font-family:"Roboto",Arial,sans-serif;
  background:linear-gradient(to bottom,var(--stage-light) 0,var(--stage-light) 664px,var(--stage-dark) 664px,var(--stage-dark) 100%);
  position:relative;color:var(--ink);
}
.page{
  position:absolute;top:80px;width:494px;height:698px;background:var(--white);
  box-shadow:0 4px 10px rgba(0,0,0,.25);overflow:hidden;
}
.page--front{left:89px}
.page--back{left:617px}
.page__art{position:absolute;inset:0;width:494px;height:698px}

.brand-box{position:absolute;left:0;top:32px;width:196px;height:68px}
.wordmark{position:absolute;color:var(--white);font-weight:500;text-transform:uppercase;line-height:1}
.wordmark__name{display:block;letter-spacing:.5px}
.wordmark__sub{display:block;letter-spacing:7px}
.wordmark--small{left:22px;top:47px}
.wordmark--small .wordmark__name{font-size:21px}
.wordmark--small .wordmark__sub{font-size:9px;margin-top:4px;letter-spacing:6.4px}
.wordmark--large{left:0;right:0;top:132px;text-align:center}
.wordmark--large .wordmark__name{font-size:40px}
.wordmark--large .wordmark__sub{font-size:15px;margin-top:6px;letter-spacing:10px}

.section-title{position:absolute;font-size:22px;font-weight:300;color:var(--brand-red);text-transform:uppercase;line-height:1}
.section-title strong{font-weight:700}
.about-title{left:34px;top:291px}
.about-text{position:absolute;left:34px;top:318px;width:432px;font-size:7.2px;line-height:9.6px;color:#333}

.whatwedo-title{left:218px;top:399px;color:var(--white)}
.feature{position:absolute;left:218px;width:262px;color:var(--white)}
.feature__tick{position:absolute;left:0;top:0;width:17px;height:17px}
.feature__title{margin-left:28px;font-size:8px;font-weight:500;text-transform:uppercase;line-height:10px}
.feature__text{margin-left:28px;font-size:7.6px;line-height:9.8px}

.contact{position:absolute;left:0;right:0;top:638px;height:40px;color:var(--white)}
.contact__item{position:absolute;top:0}
.contact__icon{position:absolute}
.contact__label{font-size:7px;color:var(--brand-red);line-height:9px}
.contact__value{font-size:9px;font-weight:500;line-height:12px}

.services-title{left:42px;top:291px}
.service{position:absolute;left:42px;right:30px}
.service__hex{position:absolute;left:0;top:0;width:72px;height:80px}
.service__name{position:absolute;left:93px;top:0;font-size:18px;font-weight:300;color:var(--brand-red);line-height:1}
.service__name strong{font-weight:500}
.service__text{position:absolute;left:93px;top:23px;width:330px;font-size:9px;line-height:10.4px;color:#333}
</style>
</head>
<body>

<!-- FRONT SIDE -->
<section class="page page--front">
  <svg class="page__art" viewBox="0 0 494 698">
    <defs>
      <linearGradient id="frontTeamPhoto" x1="0" y1="0" x2="1" y2="1">
        <stop offset="0" stop-color="#c9d2d3"/><stop offset=".5" stop-color="#7d8a8e"/><stop offset="1" stop-color="#b7bfc0"/>
      </linearGradient>
      <linearGradient id="frontDeskPhoto" x1="0" y1="0" x2="1" y2="1">
        <stop offset="0" stop-color="#8d959b"/><stop offset=".6" stop-color="#50575e"/><stop offset="1" stop-color="#c8c6c0"/>
      </linearGradient>
      <linearGradient id="bandFront" x1="0" y1="0" x2="0" y2="1">
        <stop offset="0" stop-color="#b9babc"/><stop offset="1" stop-color="#e6e7e8"/>
      </linearGradient>
      <linearGradient id="paperFront" x1="0" y1="0" x2="1" y2="0">
        <stop offset="0" stop-color="#e4e5e6"/><stop offset=".4" stop-color="#ffffff"/><stop offset="1" stop-color="#eeeeef"/>
      </linearGradient>
      <linearGradient id="footerFront" x1="0" y1="0" x2="0" y2="1">
        <stop offset="0" stop-color="#2c2c2e"/><stop offset="1" stop-color="#141415"/>
      </linearGradient>
    </defs>
    <rect width="494" height="698" fill="url(#paperFront)"/>
    <polygon points="0,228 247,284 494,224 494,252 247,300 0,262" fill="url(#bandFront)"/>
    <polygon role="img" aria-label="Photo of four business professionals walking through a glass walkway" points="0,0 494,0 494,224 247,284 0,228" fill="url(#frontTeamPhoto)"/>
    <rect role="img" aria-label="Photo of a person working at a busy office desk with laptop and files" x="0" y="378" width="230" height="230" fill="url(#frontDeskPhoto)"/>
    <path d="M0,606 L494,596 L494,698 L0,698 Z" fill="url(#footerFront)"/>
    <path d="M168,378 L494,360 L494,596 L170,606 C214,545 214,440 168,378 Z" fill="var(--brand-red)"/>
    <polygon points="0,32 196,32 170,100 0,100" fill="#1f2a30" opacity=".92"/>
  </svg>

  <div class="wordmark wordmark--small">
    <span class="wordmark__name">Vorquinexa</span>
    <span class="wordmark__sub">Solutions</span>
  </div>

  <h2 class="section-title about-title">About <strong>Us</strong></h2>
  <p class="about-text">Vorquinexa Solutions was born when experienced service management professionals came together with a single vision: to deliver FlowDesk with a level of customer support that no other company was able or willing to provide. We used our extensive experience and skills to create a startup that could give organizations the IT support they need to achieve their goals. As our IT consultancy firm grows, we retain this commitment to superior customer service</p>

  <h2 class="section-title whatwedo-title">What <strong>We Do</strong></h2>

  <div class="feature" style="top:433px">
    <svg class="feature__tick" viewBox="0 0 20 20"><circle cx="10" cy="10" r="9" fill="none" stroke="#fff" stroke-width="1.4"/><path d="M5.8,10.2 L8.8,13 L14.2,7.2" fill="none" stroke="#fff" stroke-width="1.6"/></svg>
    <p class="feature__title">Experienced Solution Focused Developers</p>
    <p class="feature__text">All Of Our Developers Have Vast Amounts Of Experience In FlowDesk</p>
  </div>
  <div class="feature" style="top:473px">
    <svg class="feature__tick" viewBox="0 0 20 20"><circle cx="10" cy="10" r="9" fill="none" stroke="#fff" stroke-width="1.4"/><path d="M5.8,10.2 L8.8,13 L14.2,7.2" fill="none" stroke="#fff" stroke-width="1.6"/></svg>
    <p class="feature__title">Competitive Pricing</p>
    <p class="feature__text">All Solutions Are Presented With Several Delivery Options E.G Full-Time US Developers, A Hybrid Of US + Near Shore, Or All Near Shore.</p>
  </div>
  <div class="feature" style="top:523px">
    <svg class="feature__tick" viewBox="0 0 20 20"><circle cx="10" cy="10" r="9" fill="none" stroke="#fff" stroke-width="1.4"/><path d="M5.8,10.2 L8.8,13 L14.2,7.2" fill="none" stroke="#fff" stroke-width="1.6"/></svg>
    <p class="feature__title">Superior Service</p>
    <p class="feature__text">Our Customers Come First And Our Client Retention Rate Of 98% Proves It. From Word One You Are Our Focus, Whether It Is Providing Alternative Solutions That No One Has Explored, Working With You On A Projects Price, Delivering A Finished Product By A Certain Date Etc.</p>
  </div>

  <div class="contact">
    <div class="contact__item" style="left:26px">
      <svg class="contact__icon" style="left:0;top:2px" width="24" height="26" viewBox="0 0 24 26"><path d="M4,1 L9,1 L10,7 L7,9 C8,14 11,18 15,20 L17,17 L23,19 L22,25 C10,25 1,14 4,1 Z" fill="var(--brand-red)"/></svg>
      <div style="margin-left:40px;margin-top:6px"><p class="contact__label">Phone Number</p><p class="contact__value">555.010.4821</p></div>
    </div>
    <div class="contact__item" style="left:150px">
      <svg class="contact__icon" style="left:0;top:5px" width="31" height="21" viewBox="0 0 31 21"><rect width="31" height="21" fill="var(--brand-red)"/><path d="M0,0 L15.5,12 L31,0" fill="none" stroke="#1d1d1f" stroke-width="1.6"/><path d="M0,21 L11,10 M31,21 L20,10" stroke="#1d1d1f" stroke-width="1.4"/></svg>
      <div style="margin-left:43px;margin-top:6px"><p class="contact__label">Email</p><p class="contact__value">info@vorquinexa.example</p></div>
    </div>
    <div class="contact__item" style="left:310px">
      <svg class="contact__icon" style="left:0;top:0" width="20" height="30" viewBox="0 0 20 30"><path d="M10,0 C4.5,0 0,4.3 0,9.8 C0,17 10,30 10,30 C10,30 20,17 20,9.8 C20,4.3 15.5,0 10,0 Z" fill="var(--brand-red)"/><circle cx="10" cy="9.5" r="4" fill="#1d1d1f"/></svg>
      <div style="margin-left:33px;margin-top:-1px"><p class="contact__label">Address</p><p class="contact__value">4410 Harlow Ave.<br>Suite 210 Fairbrook, OH 45012</p></div>
    </div>
  </div>
</section>

<!-- BACK SIDE -->
<section class="page page--back">
  <svg class="page__art" viewBox="0 0 494 698">
    <defs>
      <linearGradient id="backTeamPhoto" x1="0" y1="0" x2="1" y2="1">
        <stop offset="0" stop-color="#1c1c1f"/><stop offset=".5" stop-color="#3a3336"/><stop offset="1" stop-color="#242226"/>
      </linearGradient>
      <linearGradient id="bandBack" x1="0" y1="0" x2="0" y2="1">
        <stop offset="0" stop-color="#b6b7b9"/><stop offset="1" stop-color="#e4e5e6"/>
      </linearGradient>
      <linearGradient id="paperBack" x1="0" y1="0" x2="1" y2="0">
        <stop offset="0" stop-color="#ececed"/><stop offset=".45" stop-color="#ffffff"/><stop offset="1" stop-color="#e6e7e8"/>
      </linearGradient>
      <linearGradient id="footerBack" x1="0" y1="0" x2="0" y2="1">
        <stop offset="0" stop-color="#2c2c2e"/><stop offset="1" stop-color="#141415"/>
      </linearGradient>
    </defs>
    <rect width="494" height="698" fill="url(#paperBack)"/>
    <polygon points="0,204 247,264 494,204 494,236 247,288 0,236" fill="url(#bandBack)"/>
    <polygon role="img" aria-label="Dark photo of colleagues planning in front of a wall of sticky notes" points="0,0 494,0 494,204 247,264 0,204" fill="url(#backTeamPhoto)"/>
    <path d="M0,624 L494,596 L494,698 L0,698 Z" fill="url(#footerBack)"/>
  </svg>

  <div class="wordmark wordmark--large">
    <span class="wordmark__name">Vorquinexa</span>
    <span class="wordmark__sub">Solutions</span>
  </div>

  <h2 class="section-title services-title">Our <strong>Services</strong></h2>

  <div class="service" style="top:334px">
    <svg class="service__hex" viewBox="0 0 72 80"><polygon points="36,2 70,21 70,59 36,78 2,59 2,21" fill="var(--brand-red)" stroke="#fff" stroke-width="2"/><path d="M28,28 C20,28 17,35 19,41 L20,51 L30,51 L31,46 L35,46 L35,40 L38,38 L35,35 C35,31 33,28 28,28 Z" fill="none" stroke="#fff" stroke-width="2"/><rect x="33" y="22" width="18" height="12" rx="2" fill="none" stroke="#fff" stroke-width="2"/><circle cx="38" cy="28" r="1.2" fill="#fff"/><circle cx="42" cy="28" r="1.2" fill="#fff"/><circle cx="46" cy="28" r="1.2" fill="#fff"/></svg>
    <h3 class="service__name">Managed <strong>Services</strong></h3>
    <p class="service__text">The key to productivity and efficiency lies in doing only those things which need to be done. But, often companies end-up wasting time struggling with software administration and management; something than can easily be delegated to a third party. This – over a period of time, adds-up to huge operational costs which could have easily been saved.</p>
  </div>

  <div class="service" style="top:430px">
    <svg class="service__hex" viewBox="0 0 72 80"><polygon points="36,2 70,21 70,59 36,78 2,59 2,21" fill="var(--brand-red)" stroke="#fff" stroke-width="2"/><path d="M22,42 L40,24 L52,24 L52,36 L34,54 Z" fill="#fff"/><circle cx="47" cy="29" r="2" fill="var(--brand-red)"/><text x="35" y="44" font-size="11" font-weight="700" fill="var(--brand-red)" text-anchor="middle" font-family="Roboto, sans-serif" transform="rotate(-45 35 40)">$</text></svg>
    <h3 class="service__name">Implementation <strong>Services</strong></h3>
    <p class="service__text">Starting from scratch is hard and resource-consuming with any system. That's certainly the case with FlowDesk. You may have heard it can work wonders for your company, but between purchasing the service and setting it up properly is a long stretch of costly trial and error.</p>
  </div>

  <div class="service" style="top:528px">
    <svg class="service__hex" viewBox="0 0 72 80"><polygon points="36,2 70,21 70,59 36,78 2,59 2,21" fill="var(--brand-red)" stroke="#fff" stroke-width="2"/><circle cx="36" cy="30" r="4" fill="#fff"/><path d="M31,36 L41,36 L40,50 L32,50 Z" fill="#fff"/><circle cx="24" cy="34" r="3.2" fill="#fff"/><path d="M20,39 L28,39 L27,50 L21,50 Z" fill="#fff"/><circle cx="48" cy="34" r="3.2" fill="#fff"/><path d="M44,39 L52,39 L51,50 L45,50 Z" fill="#fff"/></svg>
    <h3 class="service__name">Virtual <strong>Assistance</strong></h3>
    <p class="service__text">FlowDesk is officially live for your team. The scope and initial deployment is done – your company is excited ... Now what?</p>
  </div>

  <div class="contact">
    <div class="contact__item" style="left:26px">
      <svg class="contact__icon" style="left:0;top:2px" width="24" height="26" viewBox="0 0 24 26"><path d="M4,1 L9,1 L10,7 L7,9 C8,14 11,18 15,20 L17,17 L23,19 L22,25 C10,25 1,14 4,1 Z" fill="var(--brand-red)"/></svg>
      <div style="margin-left:40px;margin-top:6px"><p class="contact__label">Phone Number</p><p class="contact__value">555.010.4821</p></div>
    </div>
    <div class="contact__item" style="left:150px">
      <svg class="contact__icon" style="left:0;top:5px" width="31" height="21" viewBox="0 0 31 21"><rect width="31" height="21" fill="var(--brand-red)"/><path d="M0,0 L15.5,12 L31,0" fill="none" stroke="#1d1d1f" stroke-width="1.6"/><path d="M0,21 L11,10 M31,21 L20,10" stroke="#1d1d1f" stroke-width="1.4"/></svg>
      <div style="margin-left:43px;margin-top:6px"><p class="contact__label">Email</p><p class="contact__value">info@vorquinexa.example</p></div>
    </div>
    <div class="contact__item" style="left:310px">
      <svg class="contact__icon" style="left:0;top:0" width="20" height="30" viewBox="0 0 20 30"><path d="M10,0 C4.5,0 0,4.3 0,9.8 C0,17 10,30 10,30 C10,30 20,17 20,9.8 C20,4.3 15.5,0 10,0 Z" fill="var(--brand-red)"/><circle cx="10" cy="9.5" r="4" fill="#1d1d1f"/></svg>
      <div style="margin-left:33px;margin-top:-1px"><p class="contact__label">Address</p><p class="contact__value">4410 Harlow Ave.<br>Suite 210 Fairbrook, OH 45012</p></div>
    </div>
  </div>
</section>

</body>
</html>
```